WordPress website design for wealth management company

A modern clean look website for a service company. This is mostly for information only, with a form to capture prospect contact information and schedule a 15 minutes call. There will be several static pages describe what services we offer, how we are different, and a blog section for posting articles and share resources. A section for client testimonials.
I want a website that is easy to understand and maintain. No proprietary plugins that cost extra. The main thing I need help is the visual layout / color palette that present a clean and professional look, select the suitable stock photos that convey the image of trust, professional, innovative, and high service.
Some websites with style I like include the following
- https://www.halbrookwealth.com/
- https://www.morvatefinancialorbits.com/
- https://tamblinfunds.com/private-equity-partners/
Also some websites in other industries with clean modern look
- https://plorvix.com/
- https://gravola.com/
- https://www.brisotelka.com/
I want the end product to be a fully functional website that I can upload into web hosting service I use and I can easily add content and maintain myself in the future.

```html
<!DOCTYPE html>
<html lang="en">
<head>
<meta charset="utf-8">
<title>Ardenmoor Wealth – Financial Advisors</title>
<link href="https://fonts.googleapis.com/css2?family=Poppins:wght@300;400;500;600;700&family=Libre+Baskerville&display=swap" rel="stylesheet">
<style>
:root{
  --purple:#5b2a86;
  --purple-dark:#4a1f70;
  --purple-soft:#e6d8f3;
  --yellow:#f7b52b;
  --ink:#2b2b33;
  --white:#fff;
}
*{box-sizing:border-box;margin:0;padding:0}
html,body{width:1200px;height:5324px;overflow:hidden}
body{position:relative;font-family:"Poppins",sans-serif;color:var(--ink);background:var(--white)}
.abs{position:absolute}
a{color:inherit;text-decoration:none}

/* brand: plain circle beside a one-colour wordmark */
.brand{position:absolute;display:flex;align-items:center;gap:12px}
.brand-dot{border-radius:50%;flex:none}
.brand-name{font-weight:600;letter-spacing:2px;line-height:1.15}
.brand.header{left:85px;top:40px}
.brand.header .brand-dot{width:40px;height:40px;background:var(--purple)}
.brand.header .brand-name{font-size:17px;color:var(--purple)}

/* nav */
.nav{position:absolute;top:58px;left:382px;display:flex;font-size:14px;font-weight:500;color:var(--ink)}
.nav a{margin-right:34px;padding-bottom:6px}
.nav a.active{border-bottom:2px solid var(--purple)}
.nav-call{position:absolute;left:1007px;top:49px;width:107px;height:35px;border-radius:18px;background:var(--purple);color:#fff;font-size:14px;display:flex;align-items:center;justify-content:center}

/* hero */
.hero{position:absolute;left:0;top:134px;width:1200px;height:702px;background:linear-gradient(100deg,#c9b38f 0%,#b89b6c 25%,#a9b870 55%,#c9d98f 75%,#e8e3b5 100%)}
.hero-text{position:absolute;left:620px;top:124px;width:530px;text-align:center}
.hero-text .kicker{font-size:30px;font-weight:400;color:#111}
.hero-text h1{font-size:48px;font-weight:500;color:#111;line-height:1.15;white-space:nowrap}
.hero-text .lead{font-size:24px;color:#111;margin-top:6px}
.hero-btn{display:inline-flex;align-items:center;justify-content:center;margin-top:28px;width:162px;height:58px;border-radius:30px;background:var(--purple);color:#fff;font-size:15px}
.scroll-down{position:absolute;left:575px;top:812px;width:50px;height:64px;border-radius:25px;background:#fff;box-shadow:0 4px 12px rgba(0,0,0,.12);display:flex;align-items:center;justify-content:center}

/* headings */
.sec-head{position:absolute;text-align:center}
.sec-icon{width:58px;height:58px;border:6px solid var(--purple);border-radius:50%;margin:0 auto 14px}
.sec-head h2{font-size:40px;font-weight:600;color:var(--purple);line-height:1.1;letter-spacing:.5px}
.sec-sub{display:flex;align-items:center;justify-content:center;gap:16px;margin-top:8px;color:var(--yellow);font-size:22px}
.sec-sub::before,.sec-sub::after{content:"";width:88px;height:2px;background:var(--purple)}

/* services */
.svc{position:absolute;left:85px;width:371px;height:82px;border-radius:10px;background:#fff;border:2px solid var(--purple-soft);box-shadow:0 4px 12px rgba(91,42,134,.12);display:flex;align-items:center;padding-left:14px;font-size:18px;font-weight:500;color:var(--ink)}
.svc .ico{width:54px;height:54px;border:2px solid var(--purple);border-radius:8px;margin-right:32px;display:flex;align-items:center;justify-content:center}
.svc.active{background:var(--purple);color:#fff;border-color:var(--purple)}
.svc.active .ico{border-color:var(--yellow)}
.svc-connector{position:absolute;left:458px;top:1249px;width:80px;border-top:3px dotted var(--yellow)}
.svc-connector::after{content:"";position:absolute;right:-6px;top:-6px;width:9px;height:9px;border-radius:50%;background:var(--yellow)}
.svc-photo{position:absolute;left:551px;top:1204px;width:564px;height:526px;border-radius:10px;background:linear-gradient(160deg,#dfe1e3,#a9a7a4 55%,#4d4a48)}
.svc-caption{position:absolute;left:28px;right:28px;bottom:24px;text-align:center;color:#fff;font-size:15px;line-height:1.65}

/* stats */
.stats{position:absolute;left:0;top:1871px;width:1200px;height:233px;background:var(--purple)}
.stat{position:absolute;top:40px;text-align:center;color:#fff}
.stat .num{font-family:"Libre Baskerville",serif;font-size:110px;line-height:1}
.stat .lbl{font-size:14px;margin-top:18px}
.stat-div{position:absolute;top:52px;width:2px;height:134px;background:var(--yellow)}

/* different */
.diff-photo{position:absolute;left:85px;top:2317px;width:479px;height:424px;border-radius:6px;background:linear-gradient(180deg,#dcdcd6,#c9c8c0 60%,#9a9a90)}
.diff-list{position:absolute;left:630px;top:2496px;list-style:none;font-size:17px;color:#222}
.diff-list li{display:flex;align-items:center;height:35px}
.diff-list li::before{content:"";width:12px;height:12px;border:3px solid var(--purple);border-radius:50%;margin-right:14px;border-right-color:var(--yellow)}
.pill{position:absolute;display:flex;align-items:center;justify-content:center;border-radius:30px;font-size:15px;font-weight:500}
.pill.purple{background:var(--purple);color:#fff}
.pill.yellow{background:var(--yellow);color:var(--purple-dark)}

/* blog */
.post{position:absolute;top:3101px;width:316px;height:380px}
.post-photo{position:absolute;left:0;top:0;width:100%;height:318px}
.post-body{position:absolute;left:20px;top:197px;width:224px;height:183px;background:#fff;padding:16px 22px}
.post-date{font-size:12px;color:#333;display:flex;align-items:center;gap:6px}
.post-date i{width:11px;height:11px;border:1.5px solid #555;border-radius:2px;display:inline-block}
.post h3{font-size:19px;font-weight:600;color:var(--purple);margin-top:8px}
.post p{font-size:12px;line-height:1.6;color:#333;margin-top:8px}
.post .more{display:inline-block;margin-top:16px;font-size:13px;color:var(--purple);text-decoration:underline}

/* schedule */
.schedule{position:absolute;left:0;top:3645px;width:1200px;height:409px;background:linear-gradient(100deg,#5b2a86 0%,#62348c 55%,#7d5aa3 100%)}
.schedule h2{position:absolute;left:90px;top:96px;font-size:40px;font-weight:600;color:#fff}
.schedule .rule{position:absolute;left:90px;top:160px;width:90px;height:2px;background:var(--yellow)}
.schedule p{position:absolute;left:84px;top:200px;width:480px;font-size:15px;line-height:1.75;color:#fff}
.form-card{position:absolute;left:661px;top:3810px;width:454px;height:510px;border-radius:26px;background:#fff;border:3px solid #c9aee6;box-shadow:0 8px 24px rgba(91,42,134,.18)}
.field{position:absolute;left:48px;width:362px;height:58px;border:1.5px solid #e6e0ec;border-radius:29px;display:flex;align-items:center;padding-left:30px;font-size:14px;color:#555}
.field i{width:12px;height:12px;border-radius:50%;background:var(--yellow);margin-right:12px}
.submit{position:absolute;left:48px;top:421px;width:362px;height:56px;border-radius:28px;background:var(--yellow);color:#fff;font-size:15px;display:flex;align-items:center;justify-content:center}

/* testimonials */
.quote{position:absolute;top:4450px;width:316px;height:258px;background:#fff;border-radius:8px;box-shadow:0 6px 20px rgba(0,0,0,.1);text-align:center;padding:34px 36px 0}
.quote .mark{font-family:"Libre Baskerville",serif;font-size:48px;line-height:.6;color:var(--purple)}
.quote p{margin-top:18px;font-size:13px;line-height:1.6;color:#333}
.who{display:flex;align-items:center;justify-content:center;gap:10px;margin-top:22px;text-align:left}
.avatar{width:42px;height:42px;border-radius:50%;background:#c7c7c7;border:2px solid var(--purple-soft)}
.who b{display:block;font-size:13px;font-weight:600}
.who small{font-size:9px;color:#666}
.arrow-btn{position:absolute;top:4560px;width:40px;height:40px;border-radius:50%;background:#f1f1f1;box-shadow:0 2px 6px rgba(0,0,0,.1);display:flex;align-items:center;justify-content:center}

/* footer */
.footer{position:absolute;left:0;top:4844px;width:1200px;height:418px;background:var(--purple);color:#fff}
.f-brand{position:absolute;left:85px;top:150px;width:230px}
.f-brand .brand{position:static}
.f-brand .brand-dot{width:54px;height:54px;background:#fff}
.f-brand .brand-name{font-size:22px;color:#fff}
.socials{display:flex;gap:8px;margin-top:26px;padding-left:20px}
.socials span{width:34px;height:34px;border:1.5px solid #fff;border-radius:4px}
.f-col h4{font-size:20px;font-weight:500}
.f-col h4::after{content:"";display:block;width:52px;height:2px;background:var(--yellow);margin-top:12px}
.f-links{list-style:none;margin-top:30px;font-size:15px}
.f-links li{display:flex;align-items:center;height:31px}
.f-links li::before{content:"";width:11px;height:11px;border:2.5px solid #fff;border-right-color:var(--yellow);border-radius:50%;margin-right:8px}
.c-row{position:absolute;left:0;display:flex;gap:14px;font-size:14px;line-height:1.25}
.c-ico{width:28px;height:28px;border:1.5px solid #fff;border-radius:4px;display:flex;align-items:center;justify-content:center;flex:none}
.copy{position:absolute;left:0;top:5262px;width:1200px;height:62px;background:var(--yellow);color:var(--purple-dark);font-size:13px;display:flex;align-items:center;justify-content:center}
</style>
</head>
<body>

<header>
  <div class="brand header">
    <span class="brand-dot"></span>
    <div class="brand-name">ARDENMOOR<br>WEALTH</div>
  </div>
  <nav class="nav">
    <a class="active" href="#">HOME</a>
    <a href="#">ABOUT US</a>
    <a href="#">SERVICES</a>
    <a href="#">BLOG</a>
    <a href="#">TESTIMONIALS</a>
    <a href="#">CONTACT US</a>
  </nav>
  <a class="nav-call" href="#">CALL NOW</a>
</header>

<section class="hero" role="img" aria-label="Photo of a vintage alarm clock beside stacks of coins with young plants growing, on a sunny green background">
  <div class="hero-text">
    <div class="kicker">WELCOME TO</div>
    <h1>ARDENMOOR WEALTH</h1>
    <div class="lead">FINANCIAL ADVISORS HELPING YOU</div>
    <a class="hero-btn" href="#">CALL NOW</a>
  </div>
</section>
<div class="scroll-down">
  <svg width="20" height="32" viewBox="0 0 20 32" fill="none" stroke="#5b2a86" stroke-width="2"><path d="M10 2v26M3 21l7 7 7-7"/></svg>
</div>

<div class="sec-head" style="left:300px;top:967px;width:600px">
  <div class="sec-icon"></div>
  <h2>SERVICES WE OFFER</h2>
  <div class="sec-sub">WHAT WE DO</div>
</div>

<div class="svc active" style="top:1204px"><span class="ico"><svg width="28" height="28" viewBox="0 0 28 28" fill="none" stroke="#f7b52b" stroke-width="2"><circle cx="14" cy="11" r="7"/><path d="M4 24h20"/></svg></span>Financial Planning</div>
<div class="svc-connector"></div>
<div class="svc" style="top:1312px"><span class="ico"><svg width="28" height="28" viewBox="0 0 28 28" fill="none" stroke="#5b2a86" stroke-width="2"><circle cx="14" cy="14" r="10"/><circle cx="14" cy="14" r="4"/></svg></span>Retirement Planning</div>
<div class="svc" style="top:1418px"><span class="ico"><svg width="28" height="28" viewBox="0 0 28 28" fill="none" stroke="#5b2a86" stroke-width="2"><rect x="7" y="4" width="14" height="20" rx="2"/><path d="M11 10h6M11 15h6"/></svg></span>Estate Planning</div>
<div class="svc" style="top:1524px"><span class="ico"><svg width="28" height="28" viewBox="0 0 28 28" fill="none" stroke="#5b2a86" stroke-width="2"><circle cx="14" cy="9" r="6"/><path d="M3 22c4-3 8-3 11-1h8"/></svg></span>Investment Management</div>
<div class="svc" style="top:1642px"><span class="ico"><svg width="28" height="28" viewBox="0 0 28 28" fill="none" stroke="#5b2a86" stroke-width="2"><rect x="5" y="4" width="18" height="20" rx="2"/><path d="M9 10h10M9 15h10M9 20h6"/></svg></span>Tax Planning</div>

<div class="svc-photo" role="img" aria-label="Photo of three women in a meeting at an office table by a large window">
  <p class="svc-caption">Lorem ipsum dolor sit amet, consectetur adipiscing elit. Quisque consectetur non dolor ac fermentum. Sed vels odales metus, eu bibendum mi. Vivamus vestibulum turpis at quam</p>
</div>

<section class="stats">
  <div class="stat" style="left:215px;width:200px"><div class="num">145</div><div class="lbl">OFFICES NATION WIDE</div></div>
  <div class="stat-div" style="left:464px"></div>
  <div class="stat" style="left:500px;width:200px"><div class="num">1.3</div><div class="lbl">MILLION CLIENTS</div></div>
  <div class="stat-div" style="left:725px"></div>
  <div class="stat" style="left:770px;width:230px"><div class="num">103</div><div class="lbl">500 PLAN SPONSORS</div></div>
</section>

<div class="diff-photo" role="img" aria-label="Photo of a family of four walking hand in hand outdoors"></div>
<div class="sec-head" style="left:620px;top:2289px;width:500px">
  <div class="sec-icon"></div>
  <h2>HOW WE ARE DIFFERENT</h2>
  <div class="sec-sub">WHY CHOOSE US</div>
</div>
<ul class="diff-list">
  <li>Private wealth management and family office</li>
  <li>CFO and liquidity management services</li>
  <li>Access to top lending structures and pricing</li>
  <li>Tax-efficient portfolios and direct private investments</li>
  <li>Sophisticated wealth, trust, and estate planning</li>
</ul>
<a class="pill purple" href="#" style="left:768px;top:2708px;width:163px;height:56px">CALL NOW</a>

<div class="sec-head" style="left:350px;top:2912px;width:500px">
  <div class="sec-icon"></div>
  <h2>LATEST BLOG</h2>
  <div class="sec-sub" style="font-size:19px">NEW &amp; UPDATES</div>
</div>

<article class="post" style="left:85px">
  <div class="post-photo" role="img" aria-label="Photo of an advisor reviewing documents with an older couple" style="background:linear-gradient(160deg,#8c7a6a,#d9d2c8 60%,#efe9e1)"></div>
  <div class="post-body">
    <div class="post-date"><i></i>July 25, 2023</div>
    <h3>Post 1 Headline</h3>
    <p>Lorem ipsum dolor sit amet, consectetur adipi</p>
    <a class="more" href="#">Read More</a>
  </div>
</article>
<article class="post" style="left:438px;width:324px">
  <div class="post-photo" role="img" aria-label="Photo of a tablet showing charts next to a keyboard and notebooks on a desk" style="background:linear-gradient(160deg,#3c3a3a,#8aa6b4 50%,#e3e3e3)"></div>
  <div class="post-body">
    <div class="post-date"><i></i>July 25, 2023</div>
    <h3>Post 2 Headline</h3>
    <p>Lorem ipsum dolor sit amet, consectetur adipi</p>
    <a class="more" href="#">Read More</a>
  </div>
</article>
<article class="post" style="left:801px;width:314px">
  <div class="post-photo" role="img" aria-label="Photo of a smiling family with a baby at home" style="background:linear-gradient(160deg,#9b6a4a,#d8b79a 55%,#efe4d6)"></div>
  <div class="post-body">
    <div class="post-date"><i></i>July 25, 2023</div>
    <h3>Post 3 Headline</h3>
    <p>Lorem ipsum dolor sit amet, consectetur adipi</p>
    <a class="more" href="#">Read More</a>
  </div>
</article>

<section class="schedule" role="img" aria-label="Purple-tinted background photo of a family at home">
  <h2>Schedule a&nbsp; 15 minutes Call</h2>
  <div class="rule"></div>
  <p>In 15 minutes we can get to know you – your situation, goals and needs – then connect you with an advisor committed to helping you pursue true wealth.</p>
  <a class="pill yellow" href="#" style="left:85px;top:306px;width:165px;height:66px">CALL NOW</a>
</section>

<form class="form-card">
  <div class="field" style="top:93px"><i></i>Enter Your Name</div>
  <div class="field" style="top:165px"><i></i>Enter Your Email</div>
  <div class="field" style="top:242px"><i></i>Enter Your Phone Number</div>
  <div class="field" style="top:322px"><i></i>Write Your Message</div>
  <div class="submit">SUBMIT NOW</div>
</form>

<div class="sec-head" style="left:85px;top:4238px;width:442px">
  <div class="sec-icon"></div>
  <h2>CLIENT TESTIMONIALS</h2>
  <div class="sec-sub" style="font-size:19px">WHAT OUR CLIENT SAYS</div>
</div>

<div class="arrow-btn" style="left:17px"><svg width="12" height="12" viewBox="0 0 12 12" fill="none" stroke="#555" stroke-width="1.6"><path d="M8 2L4 6l4 4"/></svg></div>
<div class="arrow-btn" style="left:1130px"><svg width="12" height="12" viewBox="0 0 12 12" fill="none" stroke="#555" stroke-width="1.6"><path d="M4 2l4 4-4 4"/></svg></div>

<div class="quote" style="left:85px">
  <div class="mark">“</div>
  <p>Lorem ipsum dolor sit amet, consef ghctetur adipiscing elit, sed do eiu smod tempor inci didunt ut abore et dolore magna aliqua.</p>
  <div class="who"><span class="avatar" role="img" aria-label="Client portrait"></span><div><b>Daniel Harrow</b><small>Managing Director</small></div></div>
</div>
<div class="quote" style="left:434px">
  <div class="mark">“</div>
  <p>Lorem ipsum dolor sit amet, consef ghctetur adipiscing elit, sed do eiu smod tempor inci didunt ut abore et dolore magna aliqua.</p>
  <div class="who"><span class="avatar" role="img" aria-label="Client portrait"></span><div><b>Daniel Harrow</b><small>Managing Director</small></div></div>
</div>
<div class="quote" style="left:785px">
  <div class="mark">“</div>
  <p>Lorem ipsum dolor sit amet, consef ghctetur adipiscing elit, sed do eiu smod tempor inci didunt ut abore et dolore magna aliqua.</p>
  <div class="who"><span class="avatar" role="img" aria-label="Client portrait"></span><div><b>Daniel Harrow</b><small>Managing Director</small></div></div>
</div>

<footer class="footer">
  <div class="f-brand">
    <div class="brand">
      <span class="brand-dot"></span>
      <div class="brand-name">ARDENMOOR<br>WEALTH</div>
    </div>
    <div class="socials"><span></span><span></span><span></span><span></span></div>
  </div>

  <div class="f-col abs" style="left:423px;top:128px">
    <h4>Quick Links</h4>
    <ul class="f-links">
      <li>About Us</li><li>Services</li><li>Blog</li><li>Testimonials</li><li>Contact Us</li>
    </ul>
  </div>

  <div class="f-col abs" style="left:657px;top:128px;width:260px;height:260px">
    <h4>Contact Us</h4>
    <div class="c-row" style="top:86px"><span class="c-ico"><svg width="14" height="14" viewBox="0 0 14 14" fill="none" stroke="#fff" stroke-width="1.4"><path d="M3 1l2 3-1.5 1.5a8 8 0 004 4L9 8l3 2-1 2.5C6 12.5 1.5 8 1.5 2.5z"/></svg></span><div>CALL US<br>xxxx xxxx xxxx</div></div>
    <div class="c-row" style="top:142px"><span class="c-ico"><svg width="14" height="12" viewBox="0 0 14 12" fill="none" stroke="#fff" stroke-width="1.4"><rect x="1" y="1" width="12" height="10"/><path d="M1 1l6 5 6-5"/></svg></span><div>EMAIL US<br>info@websitename.com</div></div>
    <div class="c-row" style="top:198px"><span class="c-ico"><svg width="12" height="14" viewBox="0 0 12 14" fill="none" stroke="#fff" stroke-width="1.4"><path d="M6 13s5-5 5-8A5 5 0 001 5c0 3 5 8 5 8z"/><circle cx="6" cy="5" r="1.6"/></svg></span><div>Address line Dummy Here<br>Address line Here</div></div>
  </div>

  <a class="pill yellow" href="#" style="left:954px;top:189px;width:159px;height:56px;font-size:14px">CLIENT LOGIN</a>
  <a class="pill yellow" href="#" style="left:954px;top:271px;width:159px;height:56px;font-size:14px">CALL NOW</a>
</footer>
<div class="copy">Copyright © 2023 All Rights Reserved By Company name</div>

</body>
</html>
```